Brochure design

We need a 4 page A4 brochure for our engieering companyA draft version of the text can be found in the attachments, along with the logo.The text pdf shows the general style and layout of hte text, but am very open to artistic advice.Three image placeholders should be added on pages indicated - these are not yet availableThe logo gives a good idea of the colour scheme required.For background graphics, the use of swirl patterns is desirable.Look and feel should be clean and professional, not too cluttered.Final desing shoul dbe avialable in RGB psd format, with full layers so we can modify text and images easily.

```html
<!DOCTYPE html>
<html lang="en">
<head>
<meta charset="utf-8">
<title>KTS Brochure – 4 pages</title>
<link href="https://fonts.googleapis.com/css2?family=Montserrat:wght@500;600;700;800&family=Raleway:wght@400;500;600;700&display=swap" rel="stylesheet">
<style>
:root{
  --teal:#2aa8b0;
  --teal-dark:#1f8f98;
  --green:#1f9a7a;
  --blue:#1d8fc4;
  --navy:#1c2b5a;
  --ink:#2b2f3a;
  --paper:#ffffff;
  --stage:#e9ecef;
  --footer:#2f3238;
}
*{box-sizing:border-box;margin:0;padding:0}
html,body{width:982px;height:1200px;overflow:hidden;background:var(--stage)}
body{position:relative;font-family:"Raleway",Arial,sans-serif;color:var(--ink)}
.page{position:absolute;width:406px;height:568px;background:var(--paper);overflow:hidden;box-shadow:0 2px 6px rgba(0,0,0,.18)}
.page--cover{left:68px;top:22px}
.page--tools{left:496px;top:22px}
.page--experience{left:68px;top:610px}
.page--services{left:496px;top:610px}
.media{position:absolute;display:block}
.bullets{list-style:none}
.bullets li{position:relative;padding-left:8px;font-size:6.6px;line-height:1.35;margin-bottom:3px;color:var(--ink)}
.bullets li::before{content:"›";position:absolute;left:0;top:-1px;color:var(--teal);font-weight:700;font-size:8px}
.tag{display:inline-block;font-family:"Montserrat",Arial,sans-serif;font-weight:700;font-size:8px;letter-spacing:.3px;color:#fff;background:var(--teal);padding:3px 8px}

/* Cover */
.cover__photo{left:0;top:0;width:170px;height:568px;background:linear-gradient(180deg,#9fb8cc 0%,#6f8aa6 35%,#32466a 70%,#1f2c4a 100%)}
.cover__panel{position:absolute;left:170px;top:0;width:236px;height:568px;background:linear-gradient(180deg,#f6f8fa,#eef2f5)}
.brand{position:absolute;right:26px;top:30px;display:flex;align-items:center;gap:6px}
.brand__mark{width:18px;height:18px;background:var(--blue)}
.brand__name{font-family:"Montserrat",Arial,sans-serif;font-weight:700;font-size:14px;color:var(--blue);line-height:1}
.brand__sub{font-family:"Montserrat",Arial,sans-serif;font-weight:700;font-size:6px;color:var(--blue);letter-spacing:.6px;margin-top:2px}
.cover__intro{position:absolute;left:172px;top:143px;width:206px;font-size:7px;line-height:1.4}
.cover__intro p{margin-bottom:6px}
.cover__intro em{font-weight:600}
.cover__design{position:absolute;left:168px;top:245px;width:214px}
.cover__design .tag{margin-bottom:6px}
.cover__render{left:170px;top:430px;width:236px;height:138px;background:radial-gradient(ellipse at 60% 60%,#3fc0b0 0%,#1e7fb8 45%,#17406e 80%,rgba(238,242,245,0) 100%)}

/* Tools */
.tools__head{position:absolute;left:0;top:0;width:406px;height:130px;background:linear-gradient(160deg,var(--teal) 0%,#3fbcbf 100%)}
.tools__head .tag{position:absolute;left:28px;top:18px;background:#fff;color:var(--teal-dark);font-size:9px}
.tools__lead{position:absolute;left:28px;top:40px;width:356px;color:#fff;font-size:6.6px;line-height:1.45;font-weight:600}
.tools__lead p{margin-bottom:5px}
.feature{position:absolute;left:28px;width:356px;display:flex;gap:10px}
.feature__icon{flex:0 0 44px;height:44px;display:flex;align-items:center;justify-content:center}
.feature__title{font-family:"Montserrat",Arial,sans-serif;font-weight:700;font-size:7.6px;line-height:1.2;margin-bottom:3px}
.icon--teal{background:var(--teal)}
.icon--green{background:var(--green)}
.icon--navy{background:var(--navy)}
.icon--blue{background:var(--blue)}
.title--teal{color:var(--teal-dark)}
.title--green{color:var(--green)}
.title--navy{color:var(--navy)}
.tools__photo{left:0;top:350px;width:406px;height:218px;background:linear-gradient(135deg,#3a3f48 0%,#7d7a70 45%,#e2c79a 70%,#f0ece4 100%)}

/* Experience */
.exp__photo{left:0;top:0;width:406px;height:182px;background:linear-gradient(180deg,#5d86b8 0%,#8eb1d6 55%,#4c5a70 80%,#2b3140 100%)}
.exp__banner{position:absolute;left:18px;top:28px;background:rgba(31,154,122,.88);padding:5px 10px;width:200px}
.exp__banner p{font-family:"Montserrat",Arial,sans-serif;color:#fff;font-size:9px;line-height:1.15;font-weight:500;text-transform:uppercase}
.exp__banner strong{font-weight:800;font-size:11px}
.exp__heading{position:absolute;left:0;top:150px;width:406px;background:rgba(255,255,255,.9);padding:5px 26px;font-family:"Montserrat",Arial,sans-serif;text-transform:uppercase;font-size:9.5px;line-height:1.2}
.exp__heading .hl{color:var(--green);font-weight:800}
.exp__heading .sub{color:var(--navy);font-weight:600}
.exp__grid{position:absolute;left:25px;top:206px;width:356px;display:flex;gap:4px}
.exp__col{flex:1;height:140px;color:#fff;text-align:center;padding:4px 6px}
.exp__col--tech{background:var(--teal)}
.exp__col--app{background:var(--green)}
.exp__col--thermal{background:var(--navy)}
.exp__badge{width:26px;height:26px;border-radius:50%;border:1.5px solid #fff;margin:0 auto 4px;display:flex;align-items:center;justify-content:center}
.exp__col h3{font-family:"Montserrat",Arial,sans-serif;font-weight:800;font-size:9px;line-height:1.1;margin-bottom:4px}
.exp__col p{font-size:6.3px;line-height:1.3;margin-bottom:3px}
.exp__col b{font-weight:700;display:block}
.exp__col--thermal p{margin-bottom:6px}
.exp__render{left:0;top:348px;width:406px;height:220px;background:radial-gradient(ellipse at 45% 50%,#e0b030 0%,#3ca060 30%,#1e70b0 55%,#1a2f55 75%,rgba(255,255,255,0) 100%)}

/* Services */
.srv__photo{left:0;top:0;width:406px;height:274px;background:linear-gradient(160deg,#0e2a55 0%,#1a5aa8 45%,#0b1e3e 100%)}
.srv__lead{position:absolute;left:26px;top:302px;width:356px;font-size:7px;line-height:1.4;font-style:italic;font-weight:600}
.srv__row{position:absolute;left:26px;width:360px;display:flex;gap:8px}
.srv__icon{flex:0 0 28px;height:26px;display:flex;align-items:center;justify-content:center}
.srv__title{font-family:"Montserrat",Arial,sans-serif;font-weight:700;font-size:6.6px;color:var(--teal-dark);text-transform:uppercase;margin-bottom:1px}
.srv__row .bullets li{font-size:6.2px;margin-bottom:1px;line-height:1.3}
.srv__footer{position:absolute;left:0;top:514px;width:406px;height:54px;background:var(--footer);padding:8px 26px;color:#fff}
.srv__footer .ask{font-style:italic;font-weight:700;font-size:6.8px;color:var(--teal);margin-bottom:3px}
.srv__footer p{font-size:6.6px;line-height:1.35}
</style>
</head>
<body>

<section class="page page--cover">
  <div class="media cover__photo" role="img" aria-label="Photo of an engineer in a blue hard hat installing solar panels"></div>
  <div class="cover__panel"></div>
  <div class="brand">
    <span class="brand__mark"></span>
    <div><div class="brand__name">KTS</div><div class="brand__sub">KELVIN THERMAL SYSTEMS</div></div>
  </div>
  <div class="cover__intro">
    <p>Kelvin Thermal Systems is a thermal engineering company specialising in the thermal management of electrical machines and electronic systems.</p>
    <p><em>We are pleased to offer the following services :</em></p>
    <ul class="bullets">
      <li>Design and consultancy</li>
      <li>Development, implementation and support of our custom thermal simulation tools</li>
    </ul>
  </div>
  <div class="cover__design">
    <span class="tag">DESIGN AND CONSULTANCY</span>
    <ul class="bullets">
      <li>We provide effective thermal design solutions for electrical machines and electronic systems</li>
      <li>We cover every stage of a design for feasibility studies, from concept comparisons to design optimisation</li>
      <li>We can review and improve cooling systems for existing designs</li>
      <li>We work with our own specially developed toolset or with software of customers preference</li>
      <li>We offer CFD, thermal network modelling, simple analytical analysis</li>
      <li>We are excellent collaborators and able to work closely with design teams from different technical disciplines to deliver solutions optimised towards product requirements and specifications</li>
    </ul>
  </div>
  <div class="media cover__render" role="img" aria-label="CFD render of an electric motor rotor with coloured flow lines"></div>
</section>

<section class="page page--tools">
  <div class="tools__head">
    <span class="tag">CUSTOM SIMULATION TOOLS</span>
    <div class="tools__lead">
      <p>KTS have developed a simulation workflow which allows the accuracy of CFD to be exploited and integrated with thermal simulation tools. We therefore offer a more accurate analysis of machines without compromising on speed.</p>
      <p>We are motivated to improve the speed and cost effectiveness of CFD modelling for electrical machine design. Our customised tools and workflow allow the accuracy of CFD to be exploited and integrated with quicker thermal modelling tools. This allows quick design exploration and optimisation whilst maintaining accuracy.</p>
    </div>
  </div>
  <div class="feature" style="top:146px">
    <div class="feature__icon icon--teal">
      <svg width="24" height="24" viewBox="0 0 24 24" fill="none" stroke="#fff" stroke-width="1.6"><circle cx="12" cy="12" r="4"/><circle cx="12" cy="12" r="9" stroke-dasharray="3 2.5"/></svg>
    </div>
    <div>
      <div class="feature__title title--teal">Customised FlowCore CFD toolset, tailored for electrical machines and electronics</div>
      <ul class="bullets">
        <li>Improved speed: minimised setup time</li>
        <li>Affordable: No expensive commercial licenses – costs don't scale up with computing power</li>
        <li>Greater automation: Customised workflow for electrical machines; reduced user input; parameterised analysis</li>
      </ul>
    </div>
  </div>
  <div class="feature" style="top:226px">
    <div class="feature__icon icon--green">
      <svg width="24" height="24" viewBox="0 0 24 24" fill="none" stroke="#fff" stroke-width="1.6"><rect x="4" y="4" width="16" height="12"/><path d="M9 20h6M12 16v4"/></svg>
    </div>
    <div>
      <div class="feature__title title--green">Thermal modelling using our in-house thermal network tool</div>
      <ul class="bullets">
        <li>High speed design exploration to expedite the route towards design optimisation</li>
        <li>Flexible: able to simulate conventional and novel machines, as well as incorporate innovative thermal management systems</li>
        <li>In-built library of correlations for predicting flow and loss behaviour</li>
      </ul>
    </div>
  </div>
  <div class="feature" style="top:288px">
    <div class="feature__icon icon--navy">
      <svg width="24" height="24" viewBox="0 0 24 24" fill="none" stroke="#fff" stroke-width="1.6"><path d="M5 19L19 5M5 5l14 14"/></svg>
    </div>
    <div>
      <div class="feature__title title--navy">Coupling between tools</div>
      <ul class="bullets">
        <li>Feed reduced order flow models from CFD into thermal networks</li>
        <li>Improved accuracy boundary conditions versus packages that rely on broad empirical correlations</li>
        <li>Ability to couple to wide range of thermal modelling packages including commercial codes</li>
      </ul>
    </div>
  </div>
  <div class="media tools__photo" role="img" aria-label="Photo of engineers reviewing drawings at a desk with a laptop"></div>
</section>

<section class="page page--experience">
  <div class="media exp__photo" role="img" aria-label="Photo of a power plant at dusk"></div>
  <div class="exp__banner">
    <p>Experience of working with and for companies and academic institutions <strong>across 8 countries</strong></p>
  </div>
  <div class="exp__heading">
    <div class="hl">We have a wide breadth of experiences.</div>
    <div class="sub">The tables below gives an indication</div>
  </div>
  <div class="exp__grid">
    <div class="exp__col exp__col--tech">
      <div class="exp__badge"><svg width="12" height="12" viewBox="0 0 12 12" fill="none" stroke="#fff" stroke-width="1.3"><circle cx="6" cy="6" r="3.5"/></svg></div>
      <h3>TECHNOLOGIES</h3>
      <p><b>Conventional Machines</b>Synchronous (PM, Field Wound, Reluctance) Induction</p>
      <p><b>Novel Machines</b>Hybrid technology</p>
      <p><b>Power Electronic Systems</b></p>
    </div>
    <div class="exp__col exp__col--app">
      <div class="exp__badge"><svg width="12" height="12" viewBox="0 0 12 12" fill="none" stroke="#fff" stroke-width="1.3"><path d="M2 7l3 3 5-7"/></svg></div>
      <h3>APPLICATIONS</h3>
      <p><b>Power generation:</b>Marine, stationary power plant, oil/gas offshore, hydro, wind</p>
      <p><b>Industrial:</b>pump drives, servo machines</p>
      <p><b>Traction and Propulsion:</b>EV, Marine</p>
    </div>
    <div class="exp__col exp__col--thermal">
      <div class="exp__badge"><svg width="12" height="12" viewBox="0 0 12 12" fill="none" stroke="#fff" stroke-width="1.3"><rect x="2.5" y="2.5" width="7" height="7"/></svg></div>
      <h3>THERMAL<br>MANAGEMENT</h3>
      <p>Passive and active cooling</p>
      <p>Fan driven flow</p>
      <p>Water cooling Spray cooling</p>
      <p>Jet impingement</p>
      <p>Advanced cooling measures</p>
    </div>
  </div>
  <div class="media exp__render" role="img" aria-label="CFD render of a cylindrical machine with streamlines and temperature colours"></div>
</section>

<section class="page page--services">
  <div class="media srv__photo" role="img" aria-label="Photo of server racks in a data centre lit in blue"></div>
  <p class="srv__lead">We offer a range of services, and work with our customers to offer flexible and bespoke solutions in line with their needs</p>
  <div class="srv__row" style="top:330px">
    <div class="srv__icon icon--teal"><svg width="16" height="16" viewBox="0 0 16 16" fill="none" stroke="#fff" stroke-width="1.3"><rect x="3" y="3" width="10" height="10"/><path d="M5 8h6"/></svg></div>
    <div>
      <div class="srv__title">Design services and support contracts</div>
      <ul class="bullets">
        <li>We work with you on your design project to enhance product performance using our experience, specialist toolsets and know-how</li>
        <li>We can both develop new products and improve existing ranges</li>
        <li>Able to use KTS toolset and workflow or follow company processes and design tools</li>
      </ul>
    </div>
  </div>
  <div class="srv__row" style="top:380px">
    <div class="srv__icon icon--green"><svg width="16" height="16" viewBox="0 0 16 16" fill="none" stroke="#fff" stroke-width="1.3"><rect x="3" y="3" width="10" height="7"/><path d="M6 13h4"/></svg></div>
    <div>
      <div class="srv__title">Use of KTS as "simulation house"</div>
      <ul class="bullets">
        <li>Providing simulation analysis for your projects</li>
        <li>KTS provide computing power: through our high-end cluster and access to wider range of clusters</li>
      </ul>
    </div>
  </div>
  <div class="srv__row" style="top:421px">
    <div class="srv__icon icon--blue"><svg width="16" height="16" viewBox="0 0 16 16" fill="none" stroke="#fff" stroke-width="1.3"><path d="M3 13L13 3M3 3l10 10"/></svg></div>
    <div>
      <div class="srv__title">Integration of KTS toolsets</div>
      <ul class="bullets">
        <li>Adopting toolsets to your company, including training and ongoing support</li>
        <li>Demos and evaluation periods available</li>
      </ul>
    </div>
  </div>
  <div class="srv__row" style="top:454px">
    <div class="srv__icon icon--navy"><svg width="16" height="16" viewBox="0 0 16 16" fill="none" stroke="#fff" stroke-width="1.3"><circle cx="5.5" cy="8" r="2.5"/><circle cx="10.5" cy="8" r="2.5"/></svg></div>
    <div>
      <div class="srv__title">Collaboration on development</div>
      <ul class="bullets">
        <li>Advanced simulation of cooling methods, such as spray or evaporative cooling</li>
        <li>Customisation of toolsets for special machine types or cooling arrangements</li>
      </ul>
    </div>
  </div>
  <footer class="srv__footer">
    <div class="ask">We welcome enquiries about our services, please contact us to learn more:</div>
    <p>dana.morrow@kelvin-thermal.co.uk</p>
    <p>Web: www.kelvin-thermal.co.uk</p>
  </footer>
</section>

</body>
</html>
```